Plumbing & Heating bussiness card design

i do all plumbing and heating work and need a catchy design. keep it simple but eye catching nothing gimicky
i do 24hr call outs
landlord safety checks
all aspects of plumbing and heating
boiler breakdowns
flue sure reg number 804617
i have put up my old card. not to bothered about the front but i have put up the back for the details. mobile number and office are the same and the email has changed to tolwenpipes@mailvoro.net

Industry/Entity Type

Safety

Contact Information for Business Card

i do 24hr call outs
landlord safety checks
boiler breakdowns

Requirements
Must have
• i do 24hr call outs
• landlord safety checks
• all aspects of plumbing and heating
• boiler breakdowns
• flue sure reg number 804617

```html
<!DOCTYPE html>
<html lang="en">
<head>
<meta charset="utf-8">
<title>R Tolwen Plumbing &amp; Heating – Business Card</title>
<link rel="stylesheet" href="https://fonts.googleapis.com/css2?family=PT+Sans:ital,wght@0,400;0,700;1,400&family=Montserrat:wght@600&display=swap">
<style>
  :root {
    --page: #e9e9e9;
    --card-front: #f4f4f4;
    --card-back: #303035;
    --ink: #3a3a3a;
    --ink-soft: #4a4a4a;
    --blue: #2f7fc4;
    --red: #b3202c;
    --light: #f2f2f2;
    --badge: #f3e21c;
    --badge-strip: #1c1c1c;
  }
  * { box-sizing: border-box; margin: 0; padding: 0; }
  html, body { width: 1105px; height: 1200px; overflow: hidden; }
  body {
    background: var(--page);
    font-family: "PT Sans", Arial, sans-serif;
    position: relative;
  }
  .card {
    position: absolute;
    left: 182px;
    width: 746px;
    height: 427px;
    overflow: hidden;
    box-shadow: 0 6px 14px rgba(0,0,0,0.18);
  }
  .card--front { top: 119px; background: var(--card-front); }
  .card--back { top: 637px; background: var(--card-back); }

  /* Front */
  .brand-name {
    position: absolute;
    left: 70px;
    top: 160px;
    width: 290px;
    text-align: center;
    color: var(--ink);
    font-weight: 700;
    line-height: 1.1;
  }
  .brand-name__main { display: block; font-size: 40px; letter-spacing: 1px; }
  .brand-name__sub { display: block; font-size: 22px; letter-spacing: 1px; margin-top: 4px; }
  .divider {
    position: absolute;
    left: 384px;
    top: 115px;
    width: 1px;
    height: 210px;
    background: #cfcfcf;
  }
  .contact {
    position: absolute;
    left: 421px;
    top: 115px;
    color: var(--ink-soft);
    font-size: 19px;
    line-height: 27px;
  }
  .contact__name {
    color: var(--blue);
    font-weight: 700;
    font-size: 27px;
    letter-spacing: 1.5px;
    margin-bottom: 14px;
  }
  .contact__address { margin-bottom: 12px; }
  .contact__line { display: flex; align-items: center; gap: 9px; height: 28px; }
  .contact__line svg { width: 17px; height: 17px; flex: none; }
  .pipe-band {
    position: absolute;
    top: 393px;
    height: 8px;
  }
  .pipe-band--red { left: 0; width: 590px; background: var(--red); }
  .pipe-band--blue { left: 652px; width: 94px; background: var(--blue); }

  /* Back */
  .back-title {
    position: absolute;
    left: 39px;
    top: 30px;
    color: var(--light);
    font-family: "Montserrat", Arial, sans-serif;
    font-weight: 600;
    font-size: 41px;
    letter-spacing: 0.5px;
    line-height: 1;
  }
  .back-title__sub {
    display: block;
    font-size: 22px;
    letter-spacing: 1.5px;
    margin-top: 6px;
    color: var(--blue);
  }
  .services {
    position: absolute;
    left: 42px;
    top: 118px;
    list-style: none;
    color: var(--light);
    font-style: italic;
    font-size: 20.5px;
    line-height: 31.4px;
  }
  .services li { position: relative; padding-left: 24px; }
  .services li::before {
    content: "";
    position: absolute;
    left: 2px;
    top: 12px;
    width: 7px;
    height: 7px;
    border-radius: 50%;
    background: var(--blue);
  }
  .reg-badge {
    position: absolute;
    left: 627px;
    top: 18px;
    width: 91px;
  }
  .reg-badge__mark {
    width: 91px;
    height: 78px;
    background: var(--badge);
  }
  .reg-badge__number {
    display: block;
    background: var(--badge-strip);
    color: var(--light);
    font-size: 10.5px;
    font-weight: 700;
    letter-spacing: 0.3px;
    line-height: 16px;
    text-align: center;
    white-space: nowrap;
  }
  .back-brand {
    position: absolute;
    left: 290px;
    top: 280px;
    width: 430px;
    text-align: center;
    color: var(--blue);
    font-weight: 700;
    font-size: 62px;
    letter-spacing: 2px;
    line-height: 1;
  }
</style>
</head>
<body>

<section class="card card--front" aria-label="Business card front">
  <div class="brand-name">
    <span class="brand-name__main">R TOLWEN</span>
    <span class="brand-name__sub">PLUMBING &amp; HEATING</span>
  </div>

  <div class="divider"></div>

  <div class="contact">
    <p class="contact__name">RORY</p>
    <p class="contact__address">42 Fernbrook Rd<br>Tavely, TV4 2KL</p>
    <p class="contact__line">
      <svg viewBox="0 0 24 24" aria-hidden="true"><path fill="#2f7fc4" d="M6.6 10.8a15.1 15.1 0 0 0 6.6 6.6l2.2-2.2c.3-.3.7-.4 1-.2 1.1.4 2.3.6 3.6.6.6 0 1 .4 1 1V20c0 .6-.4 1-1 1A17 17 0 0 1 3 4c0-.6.4-1 1-1h3.5c.6 0 1 .4 1 1 0 1.3.2 2.5.6 3.6.1.3 0 .7-.2 1z"/></svg>
      01632 960418
    </p>
    <p class="contact__line">
      <svg viewBox="0 0 24 24" aria-hidden="true"><rect x="6" y="2" width="12" height="20" rx="2" fill="none" stroke="#2f7fc4" stroke-width="2"/><circle cx="12" cy="18.5" r="1.2" fill="#2f7fc4"/></svg>
      07700 900362
    </p>
    <p class="contact__line">
      <svg viewBox="0 0 24 24" aria-hidden="true"><rect x="2" y="5" width="20" height="14" rx="1" fill="#2f7fc4"/><path d="M3 6l9 7 9-7" fill="none" stroke="#f4f4f4" stroke-width="1.6"/></svg>
      tolwenpipes@mailvoro.net
    </p>
  </div>

  <div class="pipe-band pipe-band--red"></div>
  <div class="pipe-band pipe-band--blue"></div>
</section>

<section class="card card--back" aria-label="Business card back">
  <h1 class="back-title">R TOLWEN<span class="back-title__sub">PLUMBING &amp; HEATING</span></h1>

  <ul class="services">
    <li>All aspects of Plumbing &amp; Heating</li>
    <li>I do 24hr call outs</li>
    <li>Landlord safety checks</li>
    <li>Heating Installation</li>
    <li>Gas Safety Checks</li>
    <li>General Plumbing</li>
    <li>Bathrooms</li>
    <li>Boiler breakdowns</li>
    <li>Renewables</li>
  </ul>

  <div class="reg-badge">
    <div class="reg-badge__mark" role="img" aria-label="Flue Sure registration badge"></div>
    <span class="reg-badge__number">REGISTER: 804617</span>
  </div>

  <p class="back-brand">R TOLWEN</p>
</section>

</body>
</html>
```